Ledge Crafts one page flyer

We need a standard A4 size flyer for a new company called Ledge Crafts. We are a construction material company and sell trims, crown mouldings, baseboards and panelings.
We would like to see the design with the following information:
1. Size: A4
2. Only one front page, no design need to display on back
3. Logo (Ledge Crafts, see the attached EPS file)
4. Slogan: We offer high quality products for competitive prices.
5. Content please see the PDF file
6. The production has 2 category, one called "Crown Moulding", the other is "Wainscoting", Crown Moulding has 5 productions, wainscoting has 2 production(Details see PDF file)
6. We temporary only can provide low resolution images for 7 productions, only the winner will be provided with High Resolution images.
Look and feel
Each slider illustrates characteristics of the customer's brand and the style your logo design should communicate.

```html
<!DOCTYPE html>
<html lang="en">
<head>
<meta charset="utf-8">
<title>Ledge Crafts Flyer</title>
<link rel="stylesheet" href="https://fonts.googleapis.com/css2?family=Lato:wght@400;700;900&display=swap">
<style>
  :root {
    --orange: #e8542a;
    --orange-deep: #e4481c;
    --slate: #55616a;
    --ink: #4a5560;
    --paper: #f4f4f4;
    --white: #ffffff;
  }
  * { margin: 0; padding: 0; box-sizing: border-box; }
  html, body { width: 1030px; height: 1200px; overflow: hidden; background: #e9e9e9; }
  body { font-family: "Lato", Arial, sans-serif; }

  .flyer {
    position: relative; width: 1030px; height: 1200px; overflow: hidden;
    background: linear-gradient(180deg, #f7f7f7 0%, #f1f1f1 60%, #ececec 100%);
  }
  .header-wave { position: absolute; left: 0; top: 0; width: 1030px; height: 220px; }

  .brand { position: absolute; left: 470px; top: 58px; display: flex; align-items: center; gap: 18px; }
  .brand-square { width: 76px; height: 76px; background: var(--orange); }
  .brand-text { display: flex; flex-direction: column; }
  .brand-name {
    font-size: 56px; font-weight: 400; letter-spacing: 5px; color: var(--ink);
    line-height: 1; text-transform: uppercase;
  }
  .brand-tagline {
    margin-top: 14px; font-size: 18px; letter-spacing: 4.6px; color: #6b747b;
    text-transform: uppercase;
  }

  .headline {
    position: absolute; left: 0; top: 225px; width: 1030px; text-align: center;
    font-weight: 900; font-size: 48px; line-height: 50px; letter-spacing: -1.5px;
    color: var(--ink); text-transform: uppercase;
  }

  .product-panel {
    position: absolute; left: 43px; top: 361px; width: 397px; height: 624px;
    background: var(--orange); border-radius: 26px;
  }
  .product-panel .pointer {
    position: absolute; right: -30px; top: 272px; width: 34px; height: 74px;
  }
  .category { position: absolute; left: 47px; }
  .category-title {
    font-weight: 700; font-size: 30px; line-height: 1; margin-bottom: 14px;
    text-transform: uppercase; color: var(--white);
  }
  .product { font-weight: 700; font-size: 22px; line-height: 23px; color: var(--white); margin-bottom: 25px; }
  .crown { top: 28px; }
  .wainscot-box {
    position: absolute; left: 15px; top: 422px; width: 367px; height: 189px;
    background: var(--white); border-radius: 0 0 16px 16px;
  }
  .wainscot-box .category { left: 32px; top: 22px; }
  .wainscot-box .category-title, .wainscot-box .product { color: var(--orange); }

  .product-gallery {
    position: absolute; left: 481px; top: 413px; width: 528px; height: 420px;
    background: radial-gradient(ellipse at center, #ffffff 0%, #f1f1f1 70%, rgba(240,240,240,0) 100%);
    border-radius: 12px;
  }

  .hours-tab {
    position: absolute; left: 688px; top: 848px; width: 270px; height: 38px;
    background: var(--orange); color: var(--white); text-align: center;
    font-size: 27px; line-height: 40px; text-transform: uppercase;
    clip-path: polygon(6% 0, 94% 0, 100% 100%, 0 100%); border-radius: 10px 10px 0 0;
  }
  .hours-box {
    position: absolute; left: 649px; top: 885px; width: 349px; height: 100px;
    background: var(--slate); border-radius: 14px; color: var(--white);
    text-align: center; font-size: 19px; line-height: 24px; padding-top: 12px;
  }

  .contact-tab {
    position: absolute; left: 303px; top: 1032px; width: 426px; height: 39px;
    background: var(--orange); color: var(--white); text-align: center;
    font-size: 27px; line-height: 41px; text-transform: uppercase;
    clip-path: polygon(5% 0, 95% 0, 100% 100%, 0 100%); border-radius: 10px 10px 0 0;
  }
  .contact-band {
    position: absolute; left: 0; top: 1070px; width: 1030px; height: 100px;
    background: var(--slate); color: var(--white);
  }
  .contact-col { position: absolute; top: 18px; font-size: 18.5px; line-height: 22px; }
  .contact-col .label { text-transform: uppercase; margin-bottom: 1px; }
  .contact-office { left: 48px; }
  .contact-warehouse { left: 586px; }
</style>
</head>
<body>
<main class="flyer">
  <svg class="header-wave" viewBox="0 0 1030 220" aria-hidden="true">
    <defs>
      <linearGradient id="waveFill" x1="0" y1="0" x2="1" y2="0">
        <stop offset="0" stop-color="#ffffff"/>
        <stop offset="1" stop-color="#e4e4e4"/>
      </linearGradient>
    </defs>
    <path d="M245 0 C300 110 380 170 500 172 C650 174 800 150 1030 200 L1030 0 Z" fill="url(#waveFill)"/>
    <path d="M245 0 C300 110 380 170 500 172 C650 174 800 150 1030 200" fill="none" stroke="#e4481c" stroke-width="6"/>
  </svg>

  <header class="brand">
    <div class="brand-square"></div>
    <div class="brand-text">
      <span class="brand-name">Ledge Crafts</span>
      <span class="brand-tagline">For all types of projects</span>
    </div>
  </header>

  <h1 class="headline">We offer high quality products<br>for competitive prices.</h1>

  <section class="product-panel">
    <svg class="pointer" viewBox="0 0 34 74" aria-hidden="true">
      <path d="M0 0 C8 14 34 28 34 37 C34 46 8 60 0 74 Z" fill="#e8542a"/>
    </svg>
    <div class="category crown">
      <h2 class="category-title">Crown Moulding</h2>
      <p class="product">Sienna 9 Crown Moulding<br>8 7/16"x3/4"</p>
      <p class="product">Sienna 8 Crown Moulding<br>7 3/4"x3/4"</p>
      <p class="product">Sienna 7 Crown Moulding<br>6 1/2"x3/4"</p>
      <p class="product">Lucerne 8 Crown Moulding<br>7 3/4"x3/4"</p>
      <p class="product">Lucerne 6 Crown Moulding<br>6 1/4"x3/4"</p>
    </div>
    <div class="wainscot-box">
      <div class="category">
        <h2 class="category-title">Wainscoting</h2>
        <p class="product">Colonial Chair Rail<br>3 1/4"x1"</p>
        <p class="product">Colonial Panel Mould<br>1 3/4"x5/8"</p>
      </div>
    </div>
  </section>

  <div class="product-gallery" role="img" aria-label="Five white crown moulding profiles shown at an angle"></div>

  <div class="hours-tab">Office Hours</div>
  <div class="hours-box">
    <p>Mon – Fri: 7:00am – 6.00pm</p>
    <p>Saturdays: 8:00am – 4.00pm</p>
    <p>Sundays: Closed</p>
  </div>

  <div class="contact-tab">Contact Information</div>
  <footer class="contact-band">
    <div class="contact-col contact-office">
      <p class="label">Office:</p>
      <p>214 Maple Ridge Rd, unit 7, Brookfield, Ontario L6R 2K8</p>
      <p>Phone: 905-555-0142 | hello@ledgecrafts.ca</p>
    </div>
    <div class="contact-col contact-warehouse">
      <p class="label">Warehouse:</p>
      <p>48 Foundry Lane, Eastvale, ON M5T 1A4</p>
      <p>By Appointment Only</p>
    </div>
  </footer>
</main>
</body>
</html>
```